Quantum Fern Corporate Stationary Package
Insight powered IT
Quantum Fern Corporate Stationary Package  - Information Technology
Creative Brief
Simple
Rowan Pike
CEO
PO Box R874
LKM PO
Sydney NSW 1485
AUSTRALIA
rowan@quantumfern.com.au
www.quantumfern.com.au
Letter head and email signature required
The aim is to tie the design together with 010101s and the element of the bamboo leaf.
It would be ideal if the o1o1o1 element and motif were extended into and connected with the standard layouts that are being presented to present an integrated design.
Dear Designers,
In terms of the business card, please use straight square edges, not rounded.
Please refer to the uploaded files as these contain the corporate branding.
Key elements required are:
1. Business card
2. Letter head
3. Email signature
Questions are welcome.

```html
<!DOCTYPE html>
<html lang="en">
<head>
<meta charset="utf-8">
<title>Quantum Fern — Business Card</title>
<link href="https://fonts.googleapis.com/css2?family=Arimo:wght@400;700&family=Open+Sans:wght@400;600&display=swap" rel="stylesheet">
<style>
  :root {
    --backdrop: #3b3b3b;
    --fern-green: #2c5423;
    --fern-band: #4d7446;
    --paper: #f7f7f5;
    --binary-grey: #d6d9d0;
    --logo-green: #2f5a24;
    --white: #ffffff;
  }
  * { margin: 0; padding: 0; box-sizing: border-box; }
  html, body { width: 1200px; height: 750px; overflow: hidden; }
  body {
    background: var(--backdrop);
    position: relative;
    font-family: "Arimo", Arial, sans-serif;
  }
  .card {
    position: absolute;
    top: 218px;
    width: 492px;
    height: 281px;
    overflow: hidden;
  }
  .card--front { left: 91px; background: var(--paper); }
  .card--back { left: 619px; background: var(--fern-green); }

  /* front */
  .contact-panel {
    position: absolute; left: 0; top: 0; width: 211px; height: 100%;
    background: var(--fern-green);
    color: var(--white);
    text-align: right;
  }
  .divider-line {
    position: absolute; left: 214px; top: 0; width: 4px; height: 100%;
    background: var(--fern-green);
  }
  .binary-band {
    position: absolute; left: 452px; top: 0; width: 40px; height: 100%;
    background: linear-gradient(90deg, #e6e8e2, var(--binary-grey));
  }
  .person-name { position: absolute; right: 9px; top: 55px; font-size: 13px; font-weight: 700; }
  .person-role { position: absolute; right: 9px; top: 78px; font-size: 9.5px; font-weight: 700; }
  .address { position: absolute; right: 25px; top: 106px; font-size: 10px; line-height: 16px; }
  .contact-list { position: absolute; right: 9px; top: 146px; list-style: none; }
  .contact-list li {
    display: flex; align-items: center; justify-content: flex-end;
    gap: 6px; height: 18.6px; font-size: 10.5px;
  }
  .contact-list svg { width: 12px; height: 12px; fill: var(--white); }

  .wordmark {
    position: absolute; display: flex; align-items: center; gap: 10px;
    font-family: "Open Sans", Arial, sans-serif; font-weight: 400;
    line-height: 1.05;
  }
  .wordmark__square { width: 22px; height: 22px; flex: none; }
  .wordmark__name { font-size: 28px; letter-spacing: -0.3px; }
  .card--front .wordmark { left: 248px; top: 100px; color: var(--logo-green); }
  .card--front .wordmark__square { background: var(--logo-green); }

  /* back */
  .stalk-band {
    position: absolute; left: 0; top: 0; width: 36px; height: 100%;
    background: var(--fern-band);
  }
  .card--back .wordmark { left: 292px; top: 160px; color: var(--white); }
  .card--back .wordmark__square { background: var(--white); }
  .tagline {
    position: absolute; left: 294px; top: 236px;
    font-family: "Open Sans", Arial, sans-serif;
    font-size: 15.5px; color: var(--white); letter-spacing: 0.2px;
    white-space: nowrap;
  }
</style>
</head>
<body>
  <section class="card card--front">
    <div class="contact-panel">
      <p class="person-name">Rowan Pike</p>
      <p class="person-role">CEO</p>
      <p class="address">PO Box R874, LKM PO<br>Sydney NSW 1485, AUSTRALIA</p>
      <ul class="contact-list">
        <li>+61 2 90374412
          <svg viewBox="0 0 12 12" aria-hidden="true"><path d="M3 1l2 2.5-1.2 1.3a6 6 0 0 0 3.4 3.4L8.5 7 11 9l-1.4 1.8C5.5 10.5 1.5 6.5 1.2 2.4z"/></svg></li>
        <li>+61 438 615 207
          <svg viewBox="0 0 12 12" aria-hidden="true"><path d="M3.5 0.5h5v11h-5z M4.5 1.8v6h3v-6z" fill-rule="evenodd"/></svg></li>
        <li>+61 2 93716658
          <svg viewBox="0 0 12 12" aria-hidden="true"><path d="M3 1h6v3H3z M1 5h10v5H1z M3 8h6v3H3z"/></svg></li>
        <li>rowan@quantumfern.com.au
          <svg viewBox="0 0 12 12" aria-hidden="true"><path d="M1 2.5h10v7H1z M1.5 3l4.5 3.5L10.5 3" fill="none" stroke="#fff" stroke-width="1"/></svg></li>
        <li>www.quantumfern.com.au
          <svg viewBox="0 0 12 12" aria-hidden="true"><g fill="none" stroke="#fff" stroke-width="0.9"><circle cx="6" cy="6" r="5"/><ellipse cx="6" cy="6" rx="2.2" ry="5"/><path d="M1 6h10"/></g></svg></li>
      </ul>
    </div>
    <div class="divider-line"></div>
    <div class="wordmark">
      <span class="wordmark__square"></span>
      <span class="wordmark__name">Quantum<br>Fern</span>
    </div>
    <div class="binary-band" role="img" aria-label="Column of faint 0101 binary digits"></div>
  </section>

  <section class="card card--back">
    <div class="stalk-band" role="img" aria-label="Faint leaf and stalk motif in lighter green"></div>
    <div class="wordmark">
      <span class="wordmark__square"></span>
      <span class="wordmark__name">Quantum<br>Fern</span>
    </div>
    <p class="tagline">Insight powered IT</p>
  </section>
</body>
</html>
```